Lanterns Over The Quiet Meadow Waters Book Cover

Book cover for a new book titled "Lanterns Over The Quiet Meadow Waters" which will show how retirees can pay NO tax in their retirement. Would like you to use your creative inspiration to come up with a design.

Please make MEADOW WATERS the emphasis of the title.

can you show money being rescued, or freed, from taxes.

I'm trying convey the message that retirees can FREE themselves from the burden of taxes in retirement by reading this book and following the instructions. Think about a person swimming with a weight on his back, sinking him. Suddenly the weight is removed. The feeling and imagery of the load being light now

Doing MEADOW WATERS can alleviate many of unnecessary taxes which will weight retirees down. But, unfortunately, many advisors in my industry do not educate their clients on this stuff.

Not a fan of dark backgrounds, generally speaking. Lighter is good.

Remember folks, go to brindlecart. Type in Roth IRA books. what will jump out over the stuff that's already there? Thanks!

Target Market(s)

recent, or soon to be, retirees, people in their 50s and 60s, typically couples

Industry/Entity Type

Financial

Font styles to use
Serif

Colors

Designer to choose colors to be used in the design.

Requirements
Must have
• Be optimistic, sunny, happy. How you do that? I don't know, that's why I'm hiring you. This book is designed for the lay person, (average Joe and Jane)
• Put my picture on the lower back.
• My name at bottom of the cover
Nice to have
• Be nice to have the cover POP on Brindlecart because I'm competing with so many other books and thumbnails
• Maybe a kite with a dollar bill that is breaking from a ball and chain? Just an idea.
Should not have
• No guys in suits. Happy couples sitting on the beach or sailing. That stuff is in every piece of financial planning literature.
• NOT TECHNICAL. NO PIGGY BANKS Design please

```html
<!DOCTYPE html>
<html lang="en">
<head>
<meta charset="utf-8">
<title>Lanterns Over The Quiet Meadow Waters — Book Cover</title>
<link href="https://fonts.googleapis.com/css2?family=Cinzel:wght@400;500&family=Crimson+Pro:wght@400&display=swap" rel="stylesheet">
<style>
  :root {
    --stage: #e4e4e3;
    --cover-paper: #e9eaec;
    --frame-line: #d3d5d9;
    --slate-blue: #525e8f;
    --gold-band: #c2a77b;
    --title-ink: #4d5a92;
    --author-ink: #eceef4;
  }
  * { margin: 0; padding: 0; box-sizing: border-box; }
  html, body {
    width: 1200px;
    height: 800px;
    overflow: hidden;
    background: var(--stage);
  }
  .canvas {
    position: relative;
    width: 1200px;
    height: 800px;
    display: flex;
    align-items: center;
    justify-content: center;
  }
  .book-cover {
    position: relative;
    width: 480px;
    height: 720px;
    background: var(--cover-paper);
    overflow: hidden;
  }
  .cover-frame {
    position: absolute;
    inset: 14px;
    border: 1.5px solid var(--frame-line);
  }
  .blue-column {
    position: absolute;
    left: 95px;
    top: 78px;
    width: 290px;
    height: 624px;
    background: var(--slate-blue);
  }
  .title-band {
    position: absolute;
    left: 0;
    top: 216px;
    width: 100%;
    height: 250px;
    background: var(--gold-band);
  }
  .band-rule {
    position: absolute;
    left: 0;
    width: 100%;
    height: 5px;
    background: var(--title-ink);
  }
  .band-rule--top { top: 12px; }
  .band-rule--bottom { bottom: 12px; }
  .title-block {
    position: absolute;
    inset: 0;
    display: flex;
    flex-direction: column;
    align-items: center;
    padding-top: 30px;
    color: var(--title-ink);
    text-align: center;
  }
  .title-small {
    font-family: "Cinzel", serif;
    font-size: 20px;
    font-weight: 400;
    letter-spacing: 0.04em;
    line-height: 1.1;
    text-transform: uppercase;
  }
  .title-emphasis {
    font-family: "Cinzel", serif;
    font-size: 38px;
    font-weight: 500;
    line-height: 1.05;
    padding: 3px 12px 4px;
    border-top: 2px solid var(--title-ink);
    border-bottom: 2px solid var(--title-ink);
    margin: 4px 0 2px;
  }
  .title-main {
    font-family: "Cinzel", serif;
    font-size: 38px;
    font-weight: 500;
    line-height: 1.1;
    margin-top: 2px;
  }
  .subtitle {
    font-family: "Crimson Pro", serif;
    font-size: 24px;
    font-weight: 400;
    line-height: 1.1;
    margin-top: 6px;
  }
  .author-name {
    position: absolute;
    left: 95px;
    width: 290px;
    bottom: 44px;
    font-family: "Cinzel", serif;
    font-size: 22px;
    font-weight: 400;
    line-height: 1.35;
    letter-spacing: 0.04em;
    text-align: center;
    color: var(--author-ink);
    text-transform: uppercase;
  }
</style>
</head>
<body>
  <main class="canvas">
    <article class="book-cover">
      <div class="cover-frame"></div>
      <div class="blue-column"></div>
      <section class="title-band">
        <span class="band-rule band-rule--top"></span>
        <span class="band-rule band-rule--bottom"></span>
        <div class="title-block">
          <h1 class="title-small">Lanterns Over</h1>
          <p class="title-emphasis">THE QUIET</p>
          <p class="title-main">MEADOW WATERS</p>
          <p class="subtitle">A plain plan for retirees<br>to keep every dollar free.</p>
        </div>
      </section>
      <p class="author-name">Wes<br>Harrow</p>
    </article>
  </main>
</body>
</html>
```